Business Card Design Project

We require a business card template to cover basic contact information - our company logo, names of employees, title, mobile and email.

Target Market(s)

Corporate

Industry/Entity Type

Business

Font styles to use
Sans Serif

Requirements
Nice to have
• Thinking it would be great just to have the logo taking up approximately half the space (so it goes as far across the top of the card as possible) and then contact details in the lower half of the card. Keen just to use only the two colours in the logo, on a white background.
Should not have
• No fussy drawings

```html
<!DOCTYPE html>
<html lang="en">
<head>
<meta charset="utf-8">
<title>Tidewell business card concepts</title>
<link rel="stylesheet" href="https://fonts.googleapis.com/css2?family=Jost:wght@400;500&family=Quicksand:wght@400&display=swap">
<style>
  :root {
    --canvas: #a9e9f5;
    --navy: #3467ab;
    --frame-blue: #2f7bd1;
    --teal: #34a5b9;
    --teal-text: #35a9bb;
    --sky: #4cc6ec;
    --mint: #2ecfa9;
    --white: #ffffff;
  }
  * { margin: 0; padding: 0; box-sizing: border-box; }
  html, body {
    width: 900px;
    height: 1200px;
    overflow: hidden;
    background: var(--canvas);
  }
  .sheet { position: relative; width: 900px; height: 1200px; }

  .card { position: absolute; }
  .card--classic { left: 191px; top: 34px; width: 517px; height: 312px; background: var(--navy); padding: 11px 11px 11px 11px; }
  .card--badge   { left: 191px; top: 421px; width: 517px; height: 310px; background: var(--frame-blue); padding: 11px 11px 10px 11px; }
  .card--stacked { left: 183px; top: 833px; width: 533px; height: 327px; background: var(--sky); }

  .logo-panel {
    position: relative;
    background: var(--white);
    display: flex;
    align-items: center;
    justify-content: center;
  }
  .card--classic .logo-panel { height: 164px; }
  .card--badge .logo-panel   { height: 164px; gap: 14px; }
  .card--stacked .logo-panel {
    position: absolute; left: 26px; top: 27px; width: 480px; height: 148px;
    flex-direction: column; gap: 4px;
  }

  .brand-name {
    font-family: "Jost", sans-serif;
    font-weight: 500;
    color: var(--teal-text);
    line-height: 1;
    letter-spacing: -1px;
  }
  .card--classic .brand-name { font-size: 112px; }
  .card--badge .brand-name   { font-size: 96px; }
  .card--stacked .brand-name { font-size: 56px; }

  .brand-dot { display: block; border-radius: 50%; background: var(--navy); flex: none; }
  .card--badge .brand-dot   { width: 86px; height: 86px; }
  .card--stacked .brand-dot { width: 74px; height: 74px; margin-top: -36px; }

  .contact-band {
    position: relative;
    background: var(--teal);
    color: var(--white);
  }
  .card--classic .contact-band,
  .card--badge .contact-band { height: 126px; }
  .card--stacked .contact-band {
    position: absolute; left: 0; top: 175px; width: 533px; height: 152px;
    background: var(--mint);
  }

  .role-row {
    position: absolute; left: 2px; right: 0; top: 20px;
    font-family: "Jost", sans-serif;
    font-weight: 500;
    font-size: 22px;
    color: var(--navy);
  }
  .card--stacked .role-row { left: 17px; top: 27px; }
  .role-row .role-name { position: absolute; left: 0; }
  .role-row .role-title { position: absolute; left: 261px; }
  .card--stacked .role-row .role-title { left: 261px; }

  .divider {
    position: absolute; left: 0; right: 0; top: 59px;
    height: 2px; background: var(--white);
  }
  .card--stacked .divider { left: 11px; right: 16px; top: 66px; }

  .contact-lines {
    position: absolute; left: 2px; top: 65px;
    font-family: "Quicksand", sans-serif;
    font-size: 19.5px;
    line-height: 33px;
    list-style: none;
  }
  .card--stacked .contact-lines { left: 15px; top: 74px; line-height: 36px; }
</style>
</head>
<body>
<main class="sheet">

  <article class="card card--classic">
    <div class="logo-panel">
      <span class="brand-name">Tidewell</span>
    </div>
    <div class="contact-band">
      <div class="role-row"><span class="role-name">Name</span><span class="role-title">Title</span></div>
      <div class="divider"></div>
      <ul class="contact-lines">
        <li>Mobile: 212-555-0148</li>
        <li>email: hello@tidewell.com</li>
      </ul>
    </div>
  </article>

  <article class="card card--badge">
    <div class="logo-panel">
      <span class="brand-dot"></span>
      <span class="brand-name">Tidewell</span>
    </div>
    <div class="contact-band">
      <div class="role-row"><span class="role-name">Name</span><span class="role-title">Title</span></div>
      <div class="divider"></div>
      <ul class="contact-lines">
        <li>Mobile: 212-555-0148</li>
        <li>email: hello@tidewell.com</li>
      </ul>
    </div>
  </article>

  <article class="card card--stacked">
    <div class="logo-panel">
      <span class="brand-dot"></span>
      <span class="brand-name">Tidewell</span>
    </div>
    <div class="contact-band">
      <div class="role-row"><span class="role-name">Name</span><span class="role-title">Title</span></div>
      <div class="divider"></div>
      <ul class="contact-lines">
        <li>Mobile: 212-555-0148</li>
        <li>email: hello@tidewell.com</li>
      </ul>
    </div>
  </article>

</main>
</body>
</html>
```